Staffing Company Website

We need a website for a new company based out of central California called "Harbor Field Staffing". We staff truck drivers for agriculture trucking businesses. We don't want a super corporate feel, we want something that feels more inviting to the kind of person who would work in Agriculture/Trucking while still being professional. Please let me know if you have any questions

```html
<!DOCTYPE html>
<html lang="en">
<head>
<meta charset="UTF-8">
<title>Harbor Field Staffing</title>
<link href="https://fonts.googleapis.com/css2?family=Outfit:wght@300;400;500;600;700;800&display=swap" rel="stylesheet">
<style>
:root{
  --green:#16a94a;
  --green-dark:#0f8a3b;
  --ink:#1c1c1c;
  --btn:#2b2e34;
  --muted:#555;
  --white:#fff;
  --dark-bg:#101410;
  --footer-bg:#f4f4f4;
}
*{margin:0;padding:0;box-sizing:border-box}
html,body{width:1200px;height:4420px;overflow:hidden}
body{position:relative;font-family:'Outfit',sans-serif;color:var(--ink);background:var(--white)}
.abs{position:absolute}
a{color:inherit;text-decoration:none}

/* header */
.site-header{left:0;top:0;width:1200px;height:100px;background:var(--white);z-index:5}
.brand{display:flex;align-items:center;gap:12px}
.brand-mark{width:34px;height:34px;background:var(--green);border-radius:6px}
.brand-name{font-weight:700;font-size:17px;line-height:1.05;letter-spacing:.5px;text-transform:uppercase;color:var(--ink)}
.site-header .brand{position:absolute;left:110px;top:18px}
.main-nav{position:absolute;right:72px;top:38px;display:flex;gap:34px;font-size:15px;font-weight:500;text-transform:uppercase}

/* hero */
.hero{left:0;top:100px;width:1200px;height:720px;overflow:hidden}
.hero-photo{position:absolute;inset:0;background:linear-gradient(180deg,#7fb3dd 0%,#cfe2ef 38%,#c9b37a 55%,#9b7c42 80%,#7a5e2c 100%)}
.hero-curve{position:absolute;left:0;bottom:0}
.hero-card{left:112px;top:220px;width:508px;height:340px;background:rgba(255,255,255,.55);border-radius:30px;padding:34px 36px}
.hero-card h1{font-size:58px;font-weight:800;line-height:1.02;text-transform:uppercase;color:var(--ink)}
.hero-card p{margin-top:12px;font-size:18px;line-height:1.3;color:#222;max-width:420px}
.btn{display:inline-flex;align-items:center;justify-content:center;background:var(--btn);color:var(--white);font-weight:600;text-transform:uppercase;border-radius:14px;box-shadow:6px 6px 0 rgba(0,0,0,.18)}
.hero-card .btn{position:absolute;left:36px;top:258px;width:220px;height:70px;font-size:18px}

/* section headings */
.eyebrow{color:var(--green);font-size:22px;font-weight:500}
.section-title{font-size:56px;font-weight:600;text-transform:uppercase;line-height:1}
.center-head{left:0;width:1200px;text-align:center}
.center-head .eyebrow{display:inline-flex;align-items:center;gap:12px}
.center-head .eyebrow::before,.center-head .eyebrow::after{content:"";width:70px;height:3px;background:var(--green)}

/* about */
.about-head{left:168px;top:912px}
.about-head .eyebrow{display:flex;align-items:center;gap:10px}
.about-head .eyebrow::after{content:"";width:70px;height:3px;background:var(--green)}
.about-text{left:168px;top:1010px;width:470px;font-size:15.5px;line-height:1.6;color:var(--muted)}
.about-btn{left:168px;top:1232px;width:190px;height:58px;font-size:15px}
.about-visual{left:690px;top:920px;width:340px;height:340px;border-radius:40px 0 40px 0;background:linear-gradient(135deg,#6fa8d6 0%,#a9c27a 45%,#2e8b3e 100%)}

/* services */
.services-head{top:1400px}
.services-head .section-title{margin-top:10px}
.service-card{top:1552px;width:338px;height:378px;border-radius:30px;overflow:hidden;background:linear-gradient(160deg,#8fb4cc 0%,#5a6b78 50%,#3a3f44 100%)}
.service-card .label{position:absolute;left:0;bottom:0;width:100%;height:86px;background:rgba(22,169,74,.88);color:var(--white);font-size:24px;font-weight:500;display:flex;align-items:center;justify-content:center}
.services-btn{left:488px;top:2010px;width:224px;height:72px;font-size:16px}

/* call to action */
.cta{left:0;top:2180px;width:1200px;height:520px;background:linear-gradient(180deg,#e6e6e4 0%,#d9d9d6 55%,#b9bbbb 100%)}
.cta-eyebrow{top:2310px}
.cta h2{position:absolute;left:0;top:2340px;width:1200px;text-align:center;font-size:50px;font-weight:600;line-height:1.38;color:var(--ink)}
.cta-btn{left:470px;top:2496px;width:230px;height:76px;font-size:22px;background:#0f0f0f;border-left:12px solid var(--green)}

/* testimonials */
.testi-head{top:2816px}
.testi-head .section-title{margin-top:10px}
.quote-mark{left:160px;top:2915px}
.testi-text{left:358px;top:2950px;width:740px;font-size:15.5px;line-height:1.55;color:var(--muted)}
.reviewer{left:508px;top:3090px;display:flex;align-items:center;gap:14px}
.avatar{width:50px;height:50px;border-radius:50%;background:#b8b8b8}
.reviewer strong{display:block;color:var(--green);font-size:17px;font-weight:600}
.reviewer span{font-size:13px;color:var(--muted)}
.dots{left:574px;top:3184px;display:flex;gap:10px}
.dots i{width:10px;height:10px;border-radius:50%;background:#b5b5b5}
.dots i.on{background:var(--green)}

/* contact */
.contact{left:0;top:3300px;width:1200px;height:700px;background:linear-gradient(180deg,#141a14 0%,#1f2a1c 45%,#2b3a22 75%,#1a2216 100%)}
.contact-head{left:142px;top:3432px;color:var(--white)}
.contact-head .eyebrow{display:flex;align-items:center;gap:10px}
.contact-head .eyebrow::after{content:"";width:80px;height:3px;background:var(--green)}
.contact-head .section-title{font-size:56px;margin-top:6px}
.contact-line{left:142px;display:flex;align-items:center;gap:22px;color:var(--white)}
.contact-line .ico{width:58px;height:58px;border-radius:50%;background:var(--white);display:flex;align-items:center;justify-content:center}
.contact-line small{display:block;color:var(--green);font-size:18px;font-weight:500;text-transform:uppercase}
.contact-line b{font-weight:500;font-size:22px}
.contact-form{left:508px;top:3420px;width:552px;height:382px;background:var(--green);border-radius:0 50px 0 50px;padding:44px 72px}
.field{position:absolute;background:var(--white);border-radius:4px;height:44px;font-size:12px;color:#888;padding:14px 12px}
.submit{position:absolute;left:76px;top:296px;width:178px;height:56px;font-size:14px;background:#111;box-shadow:none}
.contact-curve{left:0;top:3900px}

/* footer */
.site-footer{left:0;top:3990px;width:1200px;height:382px;background:var(--footer-bg)}
.site-footer .brand{position:absolute;left:470px;top:60px}
.site-footer .brand-mark{width:60px;height:60px;border-radius:8px}
.site-footer .brand-name{font-size:26px}
.footer-info{position:absolute;left:232px;top:200px;display:flex;gap:90px;font-size:14px}
.footer-info div{display:flex;align-items:center;gap:14px;line-height:1.3}
.footer-info .ico{width:36px;height:36px;border-radius:50%;background:#111;display:flex;align-items:center;justify-content:center}
.footer-rule{position:absolute;left:210px;top:286px;width:780px;height:1px;background:#d6d6d6}
.footer-nav{position:absolute;left:0;top:312px;width:1200px;display:flex;justify-content:center;gap:74px;font-size:14px;text-transform:uppercase}
.bottom-bar{left:0;top:4372px;width:1200px;height:48px;background:#0c0c0c;color:var(--white);font-size:12px;display:flex;align-items:center;justify-content:space-between;padding:0 70px}
.socials{display:flex;gap:8px}
.socials i{width:22px;height:22px;background:var(--white);border-radius:3px}
</style>
</head>
<body>

<header class="site-header abs">
  <div class="brand"><span class="brand-mark"></span><span class="brand-name">Harbor<br>Field<br>Staffing</span></div>
  <nav class="main-nav"><a>Home</a><a>About Us</a><a>Services</a><a>Why Choose Us</a><a>Testimonials</a><a>Contact Us</a></nav>
</header>

<section class="hero abs">
  <div class="hero-photo" role="img" aria-label="Photo of a green combine harvester working a golden wheat field under a blue sky"></div>
  <svg class="hero-curve" width="1200" height="140" viewBox="0 0 1200 140">
    <path d="M0 30 Q600 150 1200 30 L1200 140 L0 140Z" fill="#fff"/>
    <path d="M0 40 Q600 160 1200 40 L1200 70 Q600 175 0 70Z" fill="#16a94a"/>
  </svg>
</section>
<div class="hero-card abs">
  <h1>Harbor Field Staffing</h1>
  <p>Reliable drivers for farms and haulers across the Central Valley, ready when harvest calls.</p>
  <a class="btn">Apply Now</a>
</div>

<div class="about-head abs"><div class="eyebrow">Who We Are</div><h2 class="section-title">About Us</h2></div>
<p class="about-text abs">Harbor Field Staffing connects skilled truck drivers with agriculture trucking businesses throughout central California. We know the long days of harvest season, the rhythm of field to packing house, and the pride of a load delivered on time. Our team listens first, matches people with the right routes, and stays in touch so every driver and every employer feels supported from day one.</p>
<a class="btn about-btn abs">Read More</a>
<div class="about-visual abs" role="img" aria-label="Collage of farm and trucking photos"></div>

<div class="services-head center-head abs"><div class="eyebrow">What We Do</div><h2 class="section-title">Our Services</h2></div>
<div class="service-card abs" style="left:72px" role="img" aria-label="Photo of a smiling driver in a truck cab"><div class="label">Service Name 1</div></div>
<div class="service-card abs" style="left:432px" role="img" aria-label="Photo of a driver climbing into a blue truck"><div class="label">Service Name 2</div></div>
<div class="service-card abs" style="left:796px" role="img" aria-label="Photo of a driver at the wheel of a truck"><div class="label">Service Name 3</div></div>
<a class="btn services-btn abs">View More</a>

<section class="cta abs" role="img" aria-label="Faded photo of a row of parked semi trucks"></section>
<div class="cta-eyebrow center-head abs"><div class="eyebrow">Harbor Field Staffing</div></div>
<h2 class="cta-title" style="position:absolute;left:0;top:2340px;width:1200px;text-align:center;font-size:50px;font-weight:600;line-height:1.38">Are You Looking For Truck Drivers<br>For Agriculture Trucking Businesses</h2>
<a class="btn cta-btn abs">Apply Now</a>

<div class="testi-head center-head abs"><div class="eyebrow">Client Reviews</div><h2 class="section-title">Our Testimonials</h2></div>
<svg class="quote-mark abs" width="180" height="150" viewBox="0 0 180 150">
  <path d="M10 150V80Q10 20 70 5l8 18Q45 35 42 70h38v80Z" fill="#16a94a"/>
  <path d="M100 150V80Q100 20 160 5l8 18Q135 35 132 70h38v80Z" fill="#16a94a"/>
</svg>
<p class="testi-text abs">Harbor Field Staffing found us dependable drivers right before our busiest harvest in years. They took time to understand our routes, our equipment and our schedule, then sent people who showed up ready to work. Communication was clear from start to finish, and our loads kept moving without a single missed pickup. We will keep calling them every season.</p>
<div class="reviewer abs"><span class="avatar" role="img" aria-label="Reviewer portrait"></span><div><strong>Daniel Reyes</strong><span>Managing Director</span></div></div>
<div class="dots abs"><i class="on"></i><i></i><i></i></div>

<section class="contact abs" role="img" aria-label="Dark photo of a tractor in a field at dusk"></section>
<div class="contact-head abs"><div class="eyebrow">Get in touch with</div><h2 class="section-title">Contact Us</h2></div>
<div class="contact-line abs" style="top:3604px">
  <span class="ico"><svg width="26" height="26" viewBox="0 0 24 24"><path d="M6.6 10.8a15 15 0 0 0 6.6 6.6l2.2-2.2a1 1 0 0 1 1-.25 11.4 11.4 0 0 0 3.6.57 1 1 0 0 1 1 1V20a1 1 0 0 1-1 1A17 17 0 0 1 3 4a1 1 0 0 1 1-1h3.5a1 1 0 0 1 1 1c0 1.25.2 2.45.57 3.6a1 1 0 0 1-.25 1Z" fill="#111"/></svg></span>
  <div><small>Call Us</small><b>(559) 555 0142</b></div>
</div>
<div class="contact-line abs" style="top:3694px">
  <span class="ico"><svg width="26" height="26" viewBox="0 0 24 24"><path d="M3 5h18v14H3Z" fill="#111"/><path d="M3 5l9 7 9-7" stroke="#fff" stroke-width="1.6" fill="none"/></svg></span>
  <div><small>Email Us</small><b>hello@harborfieldjobs.com</b></div>
</div>
<form class="contact-form abs">
  <div class="field" style="left:72px;top:44px;width:196px">Full Name</div>
  <div class="field" style="left:284px;top:44px;width:196px">Last Name</div>
  <div class="field" style="left:72px;top:106px;width:196px">Phone</div>
  <div class="field" style="left:284px;top:106px;width:196px">Email</div>
  <div class="field" style="left:72px;top:168px;width:408px;height:106px">Message</div>
  <a class="btn submit">Submit Now</a>
</form>
<svg class="contact-curve abs" width="1200" height="110" viewBox="0 0 1200 110">
  <path d="M0 20 Q600 120 1200 20 L1200 110 L0 110Z" fill="#16a94a"/>
  <path d="M0 40 Q600 140 1200 40 L1200 110 L0 110Z" fill="#f4f4f4"/>
</svg>

<footer class="site-footer abs">
  <div class="brand"><span class="brand-mark"></span><span class="brand-name">Harbor<br>Field<br>Staffing</span></div>
  <div class="footer-info">
    <div><span class="ico"><svg width="16" height="16" viewBox="0 0 24 24"><path d="M6.6 10.8a15 15 0 0 0 6.6 6.6l2.2-2.2a1 1 0 0 1 1-.25 11.4 11.4 0 0 0 3.6.57 1 1 0 0 1 1 1V20a1 1 0 0 1-1 1A17 17 0 0 1 3 4a1 1 0 0 1 1-1h3.5a1 1 0 0 1 1 1c0 1.25.2 2.45.57 3.6a1 1 0 0 1-.25 1Z" fill="#fff"/></svg></span><span>CALL US<br>(559) 555 0142</span></div>
    <div><span class="ico"><svg width="16" height="16" viewBox="0 0 24 24"><path d="M3 5h18v14H3Z" fill="#fff"/><path d="M3 5l9 7 9-7" stroke="#111" stroke-width="1.6" fill="none"/></svg></span><span>EMAIL US<br>hello@harborfieldjobs.com</span></div>
    <div><span class="ico"><svg width="16" height="16" viewBox="0 0 24 24"><path d="M12 2a7 7 0 0 0-7 7c0 5 7 13 7 13s7-8 7-13a7 7 0 0 0-7-7Zm0 9.5A2.5 2.5 0 1 1 12 6.5a2.5 2.5 0 0 1 0 5Z" fill="#fff"/></svg></span><span>Address line Dummy Here<br>Address line Here</span></div>
  </div>
  <div class="footer-rule"></div>
  <nav class="footer-nav"><a>Home</a><a>About Us</a><a>Services</a><a>Why Choose Us?</a><a>Testimonials</a><a>Contact Us</a></nav>
</footer>
<div class="bottom-bar abs"><span>Copyright © 2024 All Rights Reserved By Harbor Field Staffing</span><span class="socials"><i></i><i></i><i></i><i></i></span></div>

</body>
</html>
```